Business Cards Brookvale
Biz_cards_Brookvale
Professional
Dwight Omsen, MD, PhD
418 Pennock Hollow Rd
Milan, TN 38358
domsen@brookvalespine.com
www.brookvalespine.com
Here is logo specs:
Brookvale Spine Institute
Fonts:
Trajan Pro (Regular)
" " " " (Bold)
Colors:
Dark Blue : R: 3 G: 34 B: 87
Light Blue : R: 0 G: 102 B: 187
Dark Red : R: 130 G: 0 B: 0
Light Green : R: 255 G: 0 B: 0

```html
<!DOCTYPE html>
<html lang="en">
<head>
<meta charset="utf-8">
<title>Brookvale Spine Institute – Business Card</title>
<link rel="stylesheet" href="https://fonts.googleapis.com/css2?family=Cinzel:wght@400;700&display=swap">
<style>
  :root {
    --dark-blue: #032257;
    --light-blue: #0066bb;
    --dark-red: #820000;
    --band-mid: #0f3a86;
    --paper: #ffffff;
    --ink: #3a3d45;
    --rule: #c9cdd4;
    --backdrop: #e9e6e1;
  }
  html, body {
    margin: 0;
    width: 1200px;
    height: 902px;
    overflow: hidden;
    background: var(--backdrop);
  }
  .card {
    position: absolute;
    left: 100px;
    top: 165px;
    width: 1000px;
    height: 572px;
    background: var(--paper);
    box-shadow: 0 10px 30px rgba(0,0,0,0.18);
    font-family: "Cinzel", "Trajan Pro", serif;
    overflow: hidden;
  }
  .brand-name {
    position: absolute;
    left: 70px;
    top: 84px;
    margin: 0;
    color: var(--dark-blue);
    font-weight: 400;
    font-size: 36px;
    letter-spacing: 2px;
    line-height: 1;
  }
  .band-rule {
    position: absolute;
    left: 0;
    right: 0;
    top: 208px;
    height: 4px;
    background: var(--rule);
  }
  .band {
    position: absolute;
    left: 0;
    right: 0;
    top: 218px;
    height: 140px;
    background: linear-gradient(180deg, var(--band-mid) 0%, var(--dark-blue) 100%);
  }
  .band-rule.lower { top: 358px; height: 3px; }
  .holder {
    position: absolute;
    right: 70px;
    top: 272px;
    color: #ffffff;
    font-size: 26px;
    letter-spacing: 1px;
  }
  .contacts {
    position: absolute;
    left: 70px;
    top: 372px;
    margin: 0;
    padding: 0;
    list-style: none;
    font-size: 16px;
    color: var(--ink);
  }
  .contacts li {
    display: flex;
    align-items: center;
    gap: 10px;
    height: 27px;
  }
  .contacts svg { width: 18px; height: 18px; flex: none; }
  .contacts .indent { padding-left: 28px; }
</style>
</head>
<body>
  <div class="card">
    <h1 class="brand-name">Brookvale Spine Institute</h1>

    <div class="band-rule"></div>
    <div class="band"></div>
    <div class="band-rule lower"></div>

    <div class="holder">Dwight Omsen, MD, PhD</div>

    <ul class="contacts">
      <li>
        <svg viewBox="0 0 18 18"><circle cx="9" cy="9" r="9" fill="#3a3d45"/><path d="M9 4a3 3 0 0 0-3 3c0 2.3 3 6 3 6s3-3.7 3-6a3 3 0 0 0-3-3z" fill="#fff"/><circle cx="9" cy="7" r="1.1" fill="#3a3d45"/></svg>
        418 Pennock Hollow Rd
      </li>
      <li class="indent">Milan, TN 38358</li>
      <li>
        <svg viewBox="0 0 18 18"><circle cx="9" cy="9" r="9" fill="#3a3d45"/><path d="M6 4.5l1.8 2.2-1 1.2a6 6 0 0 0 3.3 3.3l1.2-1 2.2 1.8-1 1.5c-3.8 0-7.5-3.7-7.5-7.5z" fill="#fff"/></svg>
        731-555-0142
      </li>
      <li>
        <svg viewBox="0 0 18 18"><circle cx="9" cy="9" r="9" fill="#3a3d45"/><rect x="6.2" y="4" width="5.6" height="10" rx="1" fill="#fff"/><rect x="7.2" y="5.2" width="3.6" height="6" fill="#3a3d45"/></svg>
        731-555-0187
      </li>
      <li>
        <svg viewBox="0 0 18 18"><circle cx="9" cy="9" r="9" fill="#3a3d45"/><path d="M6 4.5l1.8 2.2-1 1.2a6 6 0 0 0 3.3 3.3l1.2-1 2.2 1.8-1 1.5c-3.8 0-7.5-3.7-7.5-7.5z" fill="#fff"/></svg>
        1-800-555-0163
      </li>
      <li>
        <svg viewBox="0 0 18 18"><circle cx="9" cy="9" r="9" fill="#3a3d45"/><rect x="4.5" y="5.5" width="9" height="7" fill="#fff"/><path d="M4.5 5.5l4.5 4 4.5-4" fill="none" stroke="#3a3d45" stroke-width="1"/></svg>
        domsen@brookvalespine.com
      </li>
      <li>
        <svg viewBox="0 0 18 18"><circle cx="9" cy="9" r="9" fill="#3a3d45"/><circle cx="9" cy="9" r="4.8" fill="none" stroke="#fff" stroke-width="1.2"/><ellipse cx="9" cy="9" rx="2" ry="4.8" fill="none" stroke="#fff" stroke-width="1"/><line x1="4.2" y1="9" x2="13.8" y2="9" stroke="#fff" stroke-width="1"/></svg>
        www.brookvalespine.com
      </li>
    </ul>
  </div>
</body>
</html>
```